Business Card Design - Service Company

Use of the card mainly in living rooms and relations b2b We wish a card with a modern design, blue tones in the background would be a plus The card must be front / back (one side with the logo / the other with the information of contact )

Font styles to use
Serif

Requirements
Must have
• Using the map on the back of the business card Editable format! Photoshop CS2 / Illustrator CS2
Nice to have
• Maquis Vertex IT Pierre Blanche Commercial Center, 20480 Lorvanu 0495718243 Siret 71384096200018 APE 6203Y https://www.fb.com/ateliertech.maquisvertex www.maquis-vertex.com

```html
<!DOCTYPE html>
<html lang="en">
<head>
<meta charset="utf-8">
<title>Maquis Vertex IT – Business Card</title>
<link href="https://fonts.googleapis.com/css2?family=Lora:wght@400;700&display=swap" rel="stylesheet">
<style>
  :root {
    --page-bg: #e4e9ef;
    --card-top: #fbfcfd;
    --card-bottom: #eef1f5;
    --brand-blue: #1f5fa8;
    --brand-dark: #3a3c40;
    --text-grey: #55585d;
    --band-white: #ffffff;
  }
  * { margin: 0; padding: 0; box-sizing: border-box; }
  html, body { width: 1200px; height: 970px; overflow: hidden; }
  body {
    background: var(--page-bg);
    font-family: "Lora", Georgia, serif;
    position: relative;
  }
  .card {
    position: absolute;
    left: 80px; top: 188px;
    width: 1040px; height: 594px;
    background: linear-gradient(180deg, var(--card-top), var(--card-bottom));
    box-shadow: 0 12px 34px rgba(30, 50, 80, 0.18);
    overflow: hidden;
  }
  .wordmark {
    position: absolute;
    left: 530px; top: 150px;
    display: flex; align-items: center; gap: 22px;
  }
  .wordmark-square {
    width: 30px; height: 30px;
    background: var(--brand-blue);
  }
  .wordmark-name {
    font-weight: 700;
    font-size: 56px;
    line-height: 1.05;
    color: var(--brand-blue);
    letter-spacing: 1px;
  }
  .holder { position: absolute; left: 46px; top: 334px; }
  .holder-name {
    font-weight: 700; font-size: 30px; color: var(--brand-blue);
    letter-spacing: 0.5px; line-height: 1.1;
  }
  .holder-role { font-size: 26px; color: var(--text-grey); line-height: 1.05; }
  .divider {
    position: absolute; left: 44px; top: 409px;
    width: 920px; height: 2px; background: var(--brand-blue);
  }
  .contacts { position: absolute; left: 44px; top: 425px; font-size: 26px; color: var(--text-grey); }
  .contact-row { display: flex; align-items: center; gap: 12px; height: 35px; }
  .contact-icon { width: 30px; height: 30px; flex: none; }
  .legal { margin-top: 4px; }
  .address {
    position: absolute; left: 560px; top: 432px; width: 440px;
    text-align: center; font-size: 26px; color: var(--text-grey); line-height: 1.28;
  }
  .address-company { font-weight: 700; color: var(--brand-blue); }
  .bands { position: absolute; left: 0; bottom: 0; width: 1040px; height: 60px; }
  .website {
    position: absolute; left: 670px; top: 553px;
    font-size: 24px; color: var(--band-white); letter-spacing: 0.5px;
  }
</style>
</head>
<body>
  <div class="card">
    <div class="wordmark">
      <div class="wordmark-square"></div>
      <div class="wordmark-name">MAQUIS<br>VERTEX IT</div>
    </div>

    <div class="holder">
      <div class="holder-name">LUCAS MORETTI</div>
      <div class="holder-role">Director</div>
    </div>

    <div class="divider"></div>

    <div class="contacts">
      <div class="contact-row">
        <svg class="contact-icon" viewBox="0 0 30 30" aria-hidden="true">
          <circle cx="15" cy="15" r="13" fill="none" stroke="var(--brand-blue)" stroke-width="2.5"/>
          <path d="M10.5 8.5c1-.6 2 .1 2.4 1l.8 2c.3.8-.1 1.4-.7 1.9-.4.3-.4.8-.1 1.3.9 1.5 1.9 2.5 3.4 3.4.5.3 1 .3 1.3-.1.5-.6 1.1-1 1.9-.7l2 .8c.9.4 1.6 1.4 1 2.4-.9 1.5-2.6 2.1-4.3 1.4-4.2-1.7-7.3-4.8-9-9-.7-1.7-.1-3.4 1.3-4.4z" fill="var(--brand-blue)"/>
        </svg>
        <span>0495718243</span>
      </div>
      <div class="contact-row">
        <svg class="contact-icon" viewBox="0 0 30 30" aria-hidden="true">
          <circle cx="15" cy="15" r="13" fill="var(--brand-blue)"/>
        </svg>
        <span>ateliertech.maquisvertex</span>
      </div>
      <div class="legal">Siret 71384096200018 APE 6203Y</div>
    </div>

    <div class="address">
      <div class="address-company">MAQUIS VERTEX IT</div>
      <div>Pierre Blanche Commercial Center</div>
      <div>20480 Lorvanu</div>
    </div>

    <svg class="bands" viewBox="0 0 1040 60" aria-hidden="true">
      <polygon points="0,8 620,8 612,22 0,22" fill="var(--brand-dark)"/>
      <rect x="0" y="30" width="1040" height="30" fill="var(--brand-blue)"/>
      <polygon points="636,0 1040,0 1040,60 612,60" fill="var(--brand-blue)"/>
    </svg>
    <div class="website">www.maquis-vertex.com</div>
  </div>
</body>
</html>
```